I need to present the newly formed Uva Rapida concept at a board meeting in 1 weeks time. Uva Rapida is an American gas station Themed dispense concept for wine .. I need a max of 12 page power point template that incorporates a number of the photo elements of the concept and Has the uva rapida logo on each slide .. I have more pics of the concept that I will forward if you accept the project

```html
<!DOCTYPE html>
<html lang="en">
<head>
<meta charset="utf-8">
<title>Uva Rapida – Board Presentation Template</title>
<link rel="stylesheet" href="https://fonts.googleapis.com/css2?family=Rye&family=Lato:ital,wght@0,400;0,700;0,900;1,400&display=swap">
<style>
:root{
  --board:#333333;
  --red:#e5332a;
  --ink:#222222;
  --muted:#9a9a9a;
  --white:#ffffff;
  --cream:#f8ece6;
  --sage:#e4edd3;
  --navy:#47465f;
  --crimson:#d83b45;
  --blush:#f7ddd9;
  --sand:#dcd2c6;
  --salmon:#f5c6b8;
  --beige:#dccebc;
  --pale:#ededed;
  --light:#f6eee6;
}
*{box-sizing:border-box;margin:0;padding:0}
html,body{width:1200px;height:1200px;overflow:hidden;background:var(--board)}
.board{position:relative;width:1200px;height:1200px;font-family:"Lato",sans-serif}
.slide{position:absolute;width:330px;height:185px;overflow:hidden;background:var(--white)}
.shape{position:absolute;left:0;top:0;width:100%;height:100%}
.brand{position:absolute;top:14px;right:16px;font-family:"Lato",sans-serif;font-weight:900;color:var(--red);text-align:center;line-height:.9}
.brand .big{display:block;font-size:12px}
.brand .small{display:block;font-size:7px;letter-spacing:.3px}
.brand.on-dark{color:var(--light)}
.title{position:absolute;left:22px;top:17px;font-family:"Rye",serif;font-weight:400;font-size:15px;line-height:1.2;color:var(--ink);white-space:nowrap}
.title .accent{color:var(--red)}
.title.on-dark{color:var(--light)}
.page{position:absolute;right:10px;bottom:6px;font-size:11px;color:var(--muted);font-weight:400}
.cols{position:absolute;left:22px;right:38px;display:grid;grid-template-columns:1fr 1fr;column-gap:14px;font-size:4.3px;line-height:1.35;color:var(--ink)}
.cols.on-dark{color:var(--light)}
.cols ul{list-style:disc;padding-left:6px}
.cols li{margin-bottom:3.2px}
.quote{position:absolute;left:22px;top:39px;font-size:6.2px;color:var(--light);line-height:1.35}
.quote em{font-style:italic}
.lead{position:absolute;left:22px;top:70px;width:190px;font-size:8.4px;color:var(--light);line-height:1.3}
.cover{background:var(--beige);display:flex;align-items:center;justify-content:center}
.cover-mark{font-family:"Lato",sans-serif;font-weight:900;color:var(--red);text-align:center;line-height:.85}
.cover-mark .big{display:block;font-size:58px}
.cover-mark .small{display:block;font-size:34px;letter-spacing:1px}
.photo{position:absolute}
.tile-mark{position:absolute;background:var(--white);display:flex;align-items:center;justify-content:center;gap:5px}
.tile-mark .lead-in{font-family:"Rye",serif;font-size:7px;color:var(--ink)}
.tile-mark .name{font-family:"Lato",sans-serif;font-weight:900;color:var(--red);font-size:11px;line-height:.9;text-align:center}
.tile-mark .name small{display:block;font-size:7px}
.alt-label{position:absolute;left:138px;top:1020px;font-family:"Lato",sans-serif;font-weight:400;font-size:31px;color:#c9c9c9;letter-spacing:.3px}
.alt-cover{background:var(--pale)}
.alt-cover .center{position:absolute;left:38px;top:-30px;width:256px;height:245px;border-radius:50%;background:var(--white)}
.alt-cover .cover-mark{position:absolute;left:0;right:0;top:58px}
.alt-cover .cover-mark .big{font-size:44px}
.alt-cover .cover-mark .small{font-size:26px}
.band{position:absolute;left:80px;top:72px;width:180px;height:42px;background:var(--white);transform:rotate(-6deg);display:flex;align-items:center;justify-content:center;gap:8px}
.band .lead-in{font-family:"Rye",serif;font-size:9px;color:var(--ink)}
.band .name{font-family:"Lato",sans-serif;font-weight:900;color:var(--red);font-size:15px;line-height:.9;text-align:center}
.band .name small{display:block;font-size:9px}
</style>
</head>
<body>
<main class="board">

  <!-- 1 Cover -->
  <section class="slide cover" style="left:83px;top:78px">
    <div class="cover-mark"><span class="big">Uva</span><span class="small">rapida</span></div>
  </section>

  <!-- 2 Forward Drinking -->
  <section class="slide" style="left:434px;top:78px">
    <svg class="shape" viewBox="0 0 330 185" preserveAspectRatio="none" aria-hidden="true"><path fill="var(--cream)" d="M0 0H262C250 30 252 58 276 84C300 110 306 150 290 172C284 180 276 185 270 185H0Z"/></svg>
    <h2 class="title"><span class="accent">Forward Drinking</span></h2>
    <div class="brand"><span class="big">Uva</span><span class="small">rapida</span></div>
    <div class="cols" style="top:58px">
      <ul>
        <li>The global wine industry currently produces over 30 billion wine bottles each year, resulting in millions of tons of greenhouse gas and this has been flagged at a growing number of Eco forums over the last few years.</li>
        <li>The majority of the population of the developed world are Eco sceptic however over the last 3 years the environmental concerns of global wine consumers have been growing at what appears to be an alarming rate, especially when you consider the strict traditional views previously held by most of these consumers.</li>
        <li>Most if not all of the largest wine producers are radically re-thinking their long-held belief that a traditional wine approach (Glass Bottles, Corks etc) is now outdated and many of these producers are developing their production towards some form of bag-in-box style packaging which embraces a greener and more eco friendly process that puts them ahead of the consumer choice curve.</li>
      </ul>
      <ul>
        <li>The enormous rise in transportation and shipping costs over the last 3 years has also forced producers to seek packaging that allows easier transportation and increases storage capacity.</li>
        <li>Vacuum-sealed bag-in-box packaging can help preserve the wine for longer periods of time, ensuring that the product stays fresh and reduces spoilage.</li>
        <li>Finally, bag-in-box packaging often offers better value for the consumer as it tends to be less expensive than bottled wine, making it an attractive option for budget-conscious wine drinkers.</li>
      </ul>
    </div>
    <span class="page">2</span>
  </section>

  <!-- 3 More Forward Drinking -->
  <section class="slide" style="left:786px;top:78px">
    <svg class="shape" viewBox="0 0 330 185" preserveAspectRatio="none" aria-hidden="true"><path fill="var(--sage)" d="M0 0H262C250 30 252 58 276 84C300 110 306 150 290 172C284 180 276 185 270 185H0Z"/></svg>
    <h2 class="title"><span class="accent">More</span> Forward Drinking</h2>
    <div class="brand"><span class="big">Uva</span><span class="small">rapida</span></div>
    <div class="cols" style="top:58px">
      <ul>
        <li>A report produced for Cellar Review in Jan 2023 reviewed the trends that were on major producer's radars and published the following.</li>
        <li>Glass production is 10 times higher in Co2 omission terms than Bag in Box and other packaging alternatives.</li>
        <li>A 20ft container of 13,200 bottles (9,900 Ltrs) of wine produces 16,896kg of Co2 compared to 1,486kg of Co2 for a container of 3200 x 5 Ltr BIB (16,000 Ltrs).</li>
        <li>Specific key Bag in Box findings were that the quality of wine is increasing at real pace and producers will re engineer their BIB ranges and the styles and they expect a twenty-fold lift in demand as a result in the next 18 months. Most producers will use this change in an attempt to establish a clear USP for their respective brands.</li>
      </ul>
      <ul>
        <li>In the last 18 months producers are now focused on lifting BIB wine out of cheap and cheerful into the mid range and upper range of wines, including appellation controlled single varietal wines.</li>
        <li>BIB production equipment is now in high demand across Europe as producers attempt to re engineer their dispense and packaging production lines to accept BIB packaging.</li>
        <li>An interesting fact to back all of this up is that today half the consumption of wine in Sweden (eco packaging leaders) is now via BIB.</li>
      </ul>
    </div>
    <span class="page">3</span>
  </section>

  <!-- 4 Innovation -->
  <section class="slide" style="left:83px;top:292px;background:var(--crimson)">
    <svg class="shape" viewBox="0 0 330 185" preserveAspectRatio="none" aria-hidden="true"><path fill="var(--navy)" d="M0 0H275C262 40 258 80 290 110C315 135 310 170 295 185H0Z"/></svg>
    <h2 class="title on-dark">Uva Rapida: Innovation</h2>
    <div class="brand on-dark"><span class="big">Uva</span><span class="small">rapida</span></div>
    <p class="quote">Sam Hollis once said,<br><em>'Innovation distinguishes between a leader and a follower.'</em></p>
    <p class="lead">Global Retailers now need to start considering thinking “Inside The Box”</p>
    <div class="cols on-dark" style="top:104px">
      <ul>
        <li>Innovation is about creating something new and ultimately more attractive to a customer or consumer using the emerging marketing changes as the fundamental basic.</li>
        <li>Successful retailers need to be seen as a company who not only embraces change and innovation but the business needs to accept that it's crucial for driving progress and is the founding platform for ensuring the company remains highly competitive in today's ever-changing market.</li>
      </ul>
      <ul>
        <li>Uva Rapida has been working over the last eight months developing what we believe to be a highly focused eco-friendly wine dispensing concept that is not only futuristic in its approach and highly innovative but it can take advantage of the changing consumer buying trends whilst giving the warm glow of Eco consciousness by taking small steps to highlight the reduction of waste and lowering carbon emissions.</li>
        <li>The Uva Rapida brand will be firmly positioned as Uva Rapida “Wine with a Conscience”.</li>
      </ul>
    </div>
    <span class="page">4</span>
  </section>

  <!-- 5 The Brand -->
  <section class="slide" style="left:434px;top:292px;background:var(--navy)">
    <svg class="shape" viewBox="0 0 330 185" preserveAspectRatio="none" aria-hidden="true"><path fill="var(--crimson)" d="M0 0H275C262 40 258 80 290 110C315 135 310 170 295 185H0Z"/></svg>
    <h2 class="title on-dark">Uva Rapida: The Brand</h2>
    <div class="brand on-dark"><span class="big">Uva</span><span class="small">rapida</span></div>
    <div class="cols on-dark" style="top:61px">
      <ul>
        <li>As the BIB concept is currently evolving at pace it's a given that most visionaries agree that this offers an opportunity to take the BIB concept to the next level.</li>
        <li>Uva Rapida believes now is the ideal time to re-shape the future of Wine Dispensing and enhance the consumer experience.</li>
        <li>Uva Rapida will create a unique brand identity for the wine buying consumer of now and the future and will ensure the brand sits at the head of the innovation and development.</li>
        <li>Uva Rapida wine will be blended to meet the specific market consumer need for each retail business.</li>
        <li>Uva Rapida expect to deliver the biggest results in markets that currently enjoy a high percentage of loyal non-traditional retail wine BIB customers who understand and enjoy all the benefits associated with volume wine purchasing.</li>
      </ul>
      <ul>
        <li>The Uva Rapida Brand has been designed to be a clear reflection of a company's commitment to sustainability, innovation, and customer satisfaction in a crowded marketplace.</li>
        <li>The Uva Rapida dispense system is completely unique and will offer a completely new dispense offer to retail wine consumers at the same time as adding an element of novelty and fun. The concept will help enormously to differentiate a specific retail business from its competitors and is designed to enhance its reputation as a wine destination.</li>
      </ul>
    </div>
    <span class="page">5</span>
  </section>

  <!-- 6 Theatre Retailing -->
  <section class="slide" style="left:786px;top:292px">
    <svg class="shape" viewBox="0 0 330 185" preserveAspectRatio="none" aria-hidden="true"><path fill="var(--blush)" d="M0 0H262C250 30 252 58 276 84C300 110 306 150 290 172C284 180 276 185 270 185H0Z"/></svg>
    <h2 class="title"><span class="accent">Uva Rapida</span><br>Theatre Retailing</h2>
    <div class="brand"><span class="big">Uva</span><span class="small">rapida</span></div>
    <div class="cols" style="top:59px">
      <ul>
        <li>The theatre of a concept is a term used to describe the way in which a concept or idea is presented in a dramatic or theatrical manner. This can involve using various techniques such as storytelling, symbolism, and visual or audio effects to convey the essence of the concept to the audience. The aim is to create a memorable and impactful experience that engages the emotions and imagination to stimulate deeper understanding and reflection.</li>
        <li>The Uva Rapida Visual Concept will create a nostalgic 50s / 60s American Retro Gas Station. The concept theater will incorporate numerous retro signage including neon lighting, checkerboard flooring, Highway 9 style signage and various POS elements that harken back to that era. Staff in retro uniforms, aprons, and caps will help create a sense of authenticity and add to the overall theatricality of the concept.</li>
      </ul>
      <ul>
        <li>The main feature of the design will be 2 vintage style Branded Gas Pumps which will be used to dispense draught wine into 1 Ltr / 3 Ltr / 5 Ltr PETs in front of the customer. The concept will also give the customer the option of buying pre-filled PETs that will be authentically displayed as part of the concept. A return to fill option will also be offered to the customer.</li>
        <li>Overall, the key to incorporating theatrical elements into this concept is to create a sense of nostalgia and authenticity while also providing interactive and engaging experiences for customers. By combining elements such as retro decor, interactive wine dispensing systems, you can create a unique and memorable experience that will keep customers coming back.</li>
      </ul>
    </div>
    <span class="page">6</span>
  </section>

  <!-- 7 Global Logistics -->
  <section class="slide" style="left:83px;top:506px">
    <svg class="shape" viewBox="0 0 330 185" preserveAspectRatio="none" aria-hidden="true"><path fill="var(--sage)" d="M0 0H262C250 30 252 58 276 84C300 110 306 150 290 172C284 180 276 185 270 185H0Z"/></svg>
    <h2 class="title"><span class="accent">The Uva Rapida</span><br>Global Logistics</h2>
    <div class="brand"><span class="big">Uva</span><span class="small">rapida</span></div>
    <div class="cols" style="top:87px">
      <ul>
        <li>At this moment in time outline supply agreements have been made with Spain / South Africa / Italy and France.</li>
        <li>All wines shipped will have a minimum of 12 months shelf life at time of shipping.</li>
        <li>The wine will be shipped under refrigeration and in a ready to drink format.</li>
      </ul>
      <ul>
        <li>The wine will be shipped in 1,000 Ltr Eco Poly Units with 11 x 1,000 Ltr Eco Poly Units per 20ft Container.</li>
        <li>Each Poly unit will be individually palletized for ease of loading and unloading.</li>
        <li>The wine will be priced by the Ltr and this pricing will be FOB.</li>
      </ul>
    </div>
    <span class="page">7</span>
  </section>

  <!-- 8 Dispense System -->
  <section class="slide" style="left:434px;top:506px">
    <svg class="shape" viewBox="0 0 330 185" preserveAspectRatio="none" aria-hidden="true"><path fill="var(--sand)" d="M0 0H262C250 30 252 58 276 84C300 110 306 150 290 172C284 180 276 185 270 185H0Z"/></svg>
    <h2 class="title"><span class="accent">The Uva Rapida</span><br>Dispense System</h2>
    <div class="brand"><span class="big">Uva</span><span class="small">rapida</span></div>
    <div class="cols" style="top:75px">
      <ul>
        <li>3 x Stainless Steel 1000 Ltr wine storage tanks which will be used to store the wine pre dispense. 1 Tank for Red, 1 Tank for White and one tank that is used as the rotating cleaning tank.</li>
        <li>These Tanks will be directly replenished externally from a vehicle via a standard industry recognized tank pump, coupling and hosing system.</li>
        <li>These tanks will be hidden from view and located directly behind the Uva Rapida Retro concept design.</li>
        <li>The Storage tanks will be linked to a nitrogen supply which will used to create pressure in the tank and accelerate wine dispense speed. The introduction of Nitrogen removes the oxygen in the tanks and helps preserve the wine in the tanks.</li>
      </ul>
      <ul>
        <li>The Storage Tanks will be linked via a dispense pipe and a small pump to each retro style Gas Pump this will allow the wine to be dispensed to the customer via the standard filling nozzle that is attached to the Gas Pump into empty containers.</li>
        <li>The customer will also have the option to purchase pre poured 1 ltr / 3 Ltr / 5 ltr wine available at the point of dispense.</li>
        <li>The Customer will also have the option of purchasing new 1 ltr / 3Ltr / 5Ltr PETs and use these for multiple refils.</li>
      </ul>
    </div>
    <span class="page">8</span>
  </section>

  <!-- 9 Development Opportunities -->
  <section class="slide" style="left:786px;top:506px">
    <svg class="shape" viewBox="0 0 330 185" preserveAspectRatio="none" aria-hidden="true"><path fill="var(--salmon)" d="M0 0H262C250 30 252 58 276 84C300 110 306 150 290 172C284 180 276 185 270 185H0Z"/></svg>
    <h2 class="title"><span class="accent">Uva Rapida</span><br>Development Opportunities</h2>
    <div class="brand"><span class="big">Uva</span><span class="small">rapida</span></div>
    <div class="cols" style="top:87px">
      <ul>
        <li>The Uva Rapida concept is initially designed to appeal to the value wine consumer however the brand could easily develop to raise the bar in wine quality terms to include consumers who may be willing to pay a premium for better quality wine if they perceive it as a more indulgent whilst offering better value.</li>
        <li>A Uva Rapida Van housing 2 x 50Ltr Storage tanks is on the drawing board which would add a doorstep dispense option for businesses with a strong Home Delivery service.</li>
      </ul>
      <ul>
        <li>The development of a B2B business model which would see the Uva Rapida concept expand out of retail and into the On Trade.</li>
        <li>Discussions are in the early stages for Whisky Rapida and Beer Rapida which will take the concept to a new level.</li>
      </ul>
    </div>
    <span class="page">9</span>
  </section>

  <!-- 10 Photo collage -->
  <section class="slide" style="left:83px;top:721px;background:var(--white)">
    <div class="photo" role="img" aria-label="Row of vintage gas pumps in blue, orange and yellow" style="left:0;top:0;width:115px;height:104px;background:linear-gradient(90deg,#2f4d8a,#e0782c 50%,#e9c53a)"></div>
    <div class="photo" role="img" aria-label="Red wine being poured into a glass at a dark bar" style="left:0;top:106px;width:115px;height:79px;background:linear-gradient(135deg,#1c1c1c,#3a2b2a 60%,#6b1f22)"></div>
    <div class="photo" role="img" aria-label="Two red retro gas pumps under a station canopy" style="left:117px;top:0;width:103px;height:66px;background:linear-gradient(180deg,#3a3a3a,#c8303a 60%,#b9b2a8)"></div>
    <div class="tile-mark" style="left:117px;top:68px;width:103px;height:43px">
      <span class="lead-in">This is</span>
      <span class="name">Uva<small>rapida</small></span>
    </div>
    <div class="photo" role="img" aria-label="Line of colourful vintage gas pumps in a showroom" style="left:117px;top:113px;width:103px;height:72px;background:linear-gradient(90deg,#c53030,#2f4f8a 35%,#e7e2d8 55%,#c8303a)"></div>
    <div class="photo" role="img" aria-label="Retro garage interior with red pumps and wall signs" style="left:222px;top:0;width:108px;height:76px;background:linear-gradient(135deg,#4a3a2c,#8a6a4c 50%,#b3342e)"></div>
    <div class="photo" role="img" aria-label="Red and white retro pumps in a themed store" style="left:222px;top:78px;width:108px;height:107px;background:linear-gradient(160deg,#d8e3d0,#c83036 55%,#6a5442)"></div>
  </section>

  <p class="alt-label">Alternative Slides</p>

  <!-- Alternative cover -->
  <section class="slide alt-cover" style="left:432px;top:936px;width:332px;height:186px">
    <div class="center"></div>
    <div class="cover-mark"><span class="big">Uva</span><span class="small">rapida</span></div>
  </section>

  <!-- Alternative collage -->
  <section class="slide" style="left:785px;top:936px;width:332px;height:186px;background:var(--white)">
    <div class="photo" role="img" aria-label="Overlapping photos of vintage gas pumps, a retro garage and wine being poured" style="left:0;top:0;width:100%;height:100%;background:linear-gradient(120deg,#2f4d8a,#e0782c 22%,#c8303a 40%,#5a4434 62%,#c53036 80%,#e7e2d8)"></div>
    <div class="band">
      <span class="lead-in">This is</span>
      <span class="name">Uva<small>rapida</small></span>
    </div>
  </section>

</main>
</body>
</html>
```